bluegum voyages

We provide boar charter for :Fishing/whale watching and diving in Sydney Harbour providing for 12 passengersI have yet to have web page made but want to make logo first then do web page later. So I want to be able to edit and add this site to card later

Contact Information for Business Card

Captain Len (Doc) Wigellphone no 0457710098email awigell4@gmail.comCompany name Marlow Outings Pty Ltd in association with far reef cruises

Font styles to use
Serif

Requirements
Nice to have
• perhaps a photo of boat and some stick diagrams of fishing.whales and diviving

```html
<!DOCTYPE html>
<html lang="en">
<head>
<meta charset="utf-8">
<title>Marlow Outings Pty Ltd – Business Card</title>
<link rel="stylesheet" href="https://fonts.googleapis.com/css2?family=Cinzel:wght@500;700&family=Tinos&display=swap">
<style>
  :root {
    --page: #e9edf2;
    --card-white: #f7f8f8;
    --sky-blue: #5aaee0;
    --brand-blue: #2f86c9;
    --deep-blue: #1f7cc4;
    --wave-light: #4fa9e3;
    --wave-pale: #8fcaf0;
    --wave-mid: #2d8fd6;
    --ink-white: #ffffff;
    --shadow: rgba(20, 40, 70, 0.18);
  }
  * { box-sizing: border-box; margin: 0; padding: 0; }
  html, body {
    width: 1200px; height: 1000px; overflow: hidden;
    background: var(--page);
  }
  .sheet {
    position: relative; width: 1200px; height: 1000px;
    display: flex; flex-direction: column; align-items: center;
    justify-content: center; gap: 50px;
  }
  .card {
    position: relative; width: 800px; height: 450px; overflow: hidden;
    box-shadow: 0 10px 30px var(--shadow);
  }

  /* ---------- Front ---------- */
  .card-front { background: var(--card-white); }
  .front-art { position: absolute; inset: 0; }
  .company-name {
    position: absolute; top: 28px; left: 250px; width: 520px;
    text-align: center; font-family: "Cinzel", serif; line-height: 1;
  }
  .company-name .primary {
    display: block; font-size: 84px; font-weight: 700;
    color: var(--sky-blue); letter-spacing: 3px;
  }
  .company-name .secondary {
    display: block; margin-top: 8px; font-size: 42px; font-weight: 700;
    color: var(--brand-blue); letter-spacing: 2px;
  }

  /* ---------- Back ---------- */
  .card-back { background: var(--deep-blue); }
  .back-art { position: absolute; inset: 0; }
  .contact {
    position: absolute; right: 60px; top: 282px; text-align: right;
    color: var(--ink-white);
  }
  .contact .captain {
    font-family: "Cinzel", serif; font-weight: 700; font-size: 38px;
    letter-spacing: 2px; margin-bottom: 20px; line-height: 1.1;
  }
  .contact .line {
    font-family: "Tinos", serif; display: flex; align-items: center;
    justify-content: flex-end; gap: 12px; line-height: 1.15;
  }
  .contact .phone { font-size: 36px; }
  .contact .email { font-size: 27px; margin-top: 4px; }
  .contact svg { flex: none; }
</style>
</head>
<body>
<main class="sheet">

  <section class="card card-front">
    <svg class="front-art" width="800" height="450" viewBox="0 0 800 450">
      <rect class="illustration-whale-tail" x="70" y="185" width="250" height="225" rx="24"
            fill="#9aa0a5" opacity="0.55" role="img"
            aria-label="Illustration of a grey whale tail rising from splashing water"/>
      <path d="M0 395 C 120 370, 230 400, 340 380 S 560 340, 800 370 L800 450 L0 450 Z" fill="var(--wave-light)" opacity="0.55"/>
      <path d="M0 420 C 150 400, 280 430, 420 405 S 650 390, 800 410 L800 450 L0 450 Z" fill="var(--wave-mid)"/>
      <rect class="illustration-angler" x="480" y="250" width="250" height="175" rx="24"
            fill="#5c86a8" opacity="0.6" role="img"
            aria-label="Illustration of an angler in a small boat riding a wave, reeling in a fish"/>
    </svg>
    <h1 class="company-name">
      <span class="primary">MARLOW</span>
      <span class="secondary">OUTINGS PTY LTD</span>
    </h1>
  </section>

  <section class="card card-back">
    <svg class="back-art" width="800" height="450" viewBox="0 0 800 450">
      <defs>
        <linearGradient id="harbourPhoto" x1="0" y1="0" x2="0" y2="1">
          <stop offset="0" stop-color="#a9c9e6"/>
          <stop offset="0.5" stop-color="#8a9a8c"/>
          <stop offset="1" stop-color="#e6ecef"/>
        </linearGradient>
      </defs>
      <path class="photo-boats" role="img"
            aria-label="Photograph of charter boats cruising on the harbour with city buildings behind"
            d="M0 0 H800 V225 C 740 230, 700 210, 640 200 C 560 190, 520 170, 430 160 C 330 150, 250 120, 160 118 C 90 116, 40 135, 0 150 Z"
            fill="url(#harbourPhoto)"/>
      <path d="M0 150 C 40 135, 90 116, 160 118 C 250 120, 330 150, 430 160 C 520 170, 560 190, 640 200 C 700 210, 740 230, 800 225 V250 C 740 255, 700 235, 640 225 C 560 215, 520 195, 430 185 C 330 175, 250 145, 160 143 C 90 141, 40 160, 0 175 Z"
            fill="var(--wave-light)"/>
      <path d="M0 175 C 40 160, 90 141, 160 143 C 250 145, 330 175, 430 185 C 520 195, 560 215, 640 225 C 700 235, 740 255, 800 250 V268 C 740 273, 700 253, 640 243 C 560 233, 520 213, 430 203 C 330 193, 250 163, 160 161 C 90 159, 40 178, 0 193 Z"
            fill="var(--wave-pale)"/>
      <rect class="illustration-diver" x="40" y="215" width="240" height="150" rx="22"
            fill="#3f9ad8" role="img"
            aria-label="Illustration of a scuba diver swimming with fins and air tank, bubbles rising"/>
    </svg>
    <div class="contact">
      <p class="captain">CAPTAIN LEN</p>
      <p class="line phone">0468231594
        <svg width="20" height="30" viewBox="0 0 20 30" aria-hidden="true">
          <rect x="2" y="2" width="16" height="26" rx="3" fill="none" stroke="#fff" stroke-width="2.2"/>
          <circle cx="10" cy="23" r="1.6" fill="#fff"/>
        </svg>
      </p>
      <p class="line email">lpruntel7@tidewake.net
        <svg width="22" height="16" viewBox="0 0 22 16" aria-hidden="true">
          <rect x="1" y="1" width="20" height="14" fill="none" stroke="#fff" stroke-width="2"/>
          <path d="M1 1 L11 9 L21 1" fill="none" stroke="#fff" stroke-width="2"/>
        </svg>
      </p>
    </div>
  </section>

</main>
</body>
</html>
```